Plakat-Design für Blasmusik Konzert
Zielgruppe
Wir - die Tordinger Blasmusik e.V. - sind auf der Suche nach:
einem Plakatdesign in A1 & A2 und passendem
Ticket-Design DIN lang quer inkl. Perforierung und 2x Nummerierung
für unser Konzert 2019 mit dem Motto:
'NIGHTS OF WONDER'.
Das Konzert wird einen weiten Rahmen von Henrik Dallmann und Brisko hin zu Bernd Falkenrath und Tom Kellin. Auch Titel aus dem Bereich Filmmusik wird es geben. Also ein bunter Abend mit Gesang und Showlicht.
Wir freuen uns auf eure Ideen!!!
Impressionen: www.tordinger-blasmusik.de
Aufgabenstellung
Stichworte: Bunt, Modern, Edel
Facts:
Samstag 05.10.2019 Beginn 19:00
Festsaal im Bildungshaus, Kirchwerden am Teich
Eintritt 15€, Kinder bis einschließlich 8 Jahre Eintritt frei.
'Mehr Informationen unter www.tordinger-blasmusik.de und auf Plaudernet'
Für Ticket: Einlass ab 18:30 Uhr. Freie Platzwahl.
Irgendwo auf dem Plakat muss Platz für die dezente Nennung von 2-3 Sponsoren vorgesehen werden. Diese würden wir nachträglich einfügen. Auch ein 'Find us on Plaudernet'-Icon wäre cool.
Die Druckdateien (CMYK) sind mit entsprechendem Beschnitt gemäß Vorgabe von 'flott-gedruckt-jetzt' anzulegen und als Vector-Datei sowie PDF zu übergeben.

```html
<!DOCTYPE html>
<html lang="de">
<head>
<meta charset="utf-8">
<title>Nights of Wonder – Konzert 2019</title>
<link href="https://fonts.googleapis.com/css2?family=Fira+Sans:ital,wght@0,600;0,700;1,500;1,600&family=Great+Vibes&display=swap" rel="stylesheet">
<style>
  :root {
    --backdrop: #3b3e41;
    --poster-red: #8e1c22;
    --gold: #e6b94e;
    --gold-band: #e5bd52;
    --white: #ffffff;
    --purple: #6a2b8a;
    --navy: #2a2f8f;
    --footer-text: #8e1c22;
  }
  * { margin: 0; padding: 0; box-sizing: border-box; }
  html, body { width: 1200px; height: 1200px; overflow: hidden; }
  body { background: var(--backdrop); font-family: "Fira Sans", Arial, sans-serif; }

  .poster {
    position: absolute; left: 192px; top: 20px;
    width: 816px; height: 1160px;
    background: var(--poster-red);
    color: var(--white);
    overflow: hidden;
  }
  .illustration {
    position: absolute; left: 0; top: 190px; width: 816px; height: 720px;
    background:
      radial-gradient(circle at 18% 60%, rgba(42,47,143,.35), transparent 22%),
      radial-gradient(circle at 85% 30%, rgba(42,47,143,.35), transparent 18%),
      radial-gradient(circle at 30% 15%, rgba(200,40,40,.35), transparent 16%),
      radial-gradient(circle at 80% 55%, rgba(210,50,40,.35), transparent 15%),
      radial-gradient(ellipse at 50% 50%, rgba(95,15,20,.45), transparent 70%);
  }
  .club-name {
    position: absolute; left: 40px; top: 86px;
    font-weight: 700; font-style: italic; font-size: 38px; line-height: 1.05;
  }
  .event-facts { position: absolute; right: 24px; top: 30px; text-align: right; font-style: italic; }
  .event-date { color: var(--gold); font-weight: 600; font-size: 44px; line-height: 1.1; }
  .event-start { font-weight: 600; font-size: 40px; line-height: 1.1; }
  .event-rule { height: 2px; background: var(--gold); width: 285px; margin: 14px 0 10px auto; }
  .event-venue { font-weight: 600; font-size: 23px; line-height: 1.3; }

  .title {
    position: absolute; left: 0; width: 816px; text-align: center;
    font-family: "Great Vibes", cursive; font-weight: 400; line-height: 1;
    text-shadow: 0 2px 6px rgba(0,0,0,.25);
  }
  .title-top { top: 310px; font-size: 190px; }
  .title-bottom { top: 500px; font-size: 170px; }
  .subtitle {
    position: absolute; left: 250px; top: 715px;
    font-weight: 600; font-size: 38px;
  }
  .admission {
    position: absolute; left: 575px; top: 723px; width: 206px; height: 206px;
    border-radius: 50%; background: var(--purple);
    display: flex; flex-direction: column; align-items: center; justify-content: center;
    font-weight: 600; font-size: 44px; line-height: 1.2;
  }
  .program { position: absolute; left: 0; width: 816px; text-align: center; font-weight: 600; font-style: italic; }
  .program-artists { top: 940px; font-size: 30px; }
  .program-note { top: 978px; font-size: 29px; }
  .fineprint { position: absolute; left: 0; top: 1024px; width: 816px; text-align: center; font-size: 14.5px; font-style: italic; font-weight: 500; }

  .footer {
    position: absolute; left: 0; bottom: 0; width: 816px; height: 105px;
    background: var(--gold-band); color: var(--footer-text);
  }
  .footer-label { position: absolute; left: 12px; top: 10px; font-size: 14px; font-weight: 600; }
  .footer-link { position: absolute; left: 12px; font-size: 23px; font-weight: 500; font-style: italic; display: flex; align-items: center; gap: 6px; }
  .footer-link.social { top: 32px; }
  .footer-link.web { top: 62px; left: 14px; }
  .social-square { width: 16px; height: 16px; background: var(--navy); display: inline-block; }
  .sponsors { position: absolute; right: 14px; top: 24px; display: flex; gap: 9px; }
  .sponsor-badge { width: 94px; height: 58px; background: var(--white); }
</style>
</head>
<body>
  <main class="poster">
    <div class="illustration" role="img" aria-label="Illustration: stilisierte Musiker mit Trompeten, Saxophonen und Tuba in Rot, Blau und Schwarz"></div>

    <div class="club-name">Tordinger<br>Blasmusik e.V.</div>

    <div class="event-facts">
      <div class="event-date">Sa. 05.10.2019</div>
      <div class="event-start">Beginn: 19.00</div>
      <div class="event-rule"></div>
      <div class="event-venue">Festsaal im Bildungshaus<br>Kirchwerden am Teich</div>
    </div>

    <h1 class="title title-top">Nights</h1>
    <div class="title title-bottom">of Wonder</div>
    <div class="subtitle">Konzert 2019</div>

    <div class="admission"><span>Eintritt</span><span>15€*</span></div>

    <p class="program program-artists">Henrik Dallmann...Brisko...Bernd Falkenrath...Tom Kellin</p>
    <p class="program program-note">Bunter Abend mit Gesang und Showlicht</p>
    <p class="fineprint">*Kinder bis einschließlich 8 Jahre Eintritt frei. Für Ticket: Einlass ab 18:30 Uhr. Freie Platzwahl.</p>

    <footer class="footer">
      <div class="footer-label">Mehr Informationen :</div>
      <div class="footer-link social"><span class="social-square"></span>plaudernet.de/Tordinger-Blasmusik-eV</div>
      <div class="footer-link web">www.tordinger-blasmusik.de</div>
      <div class="sponsors">
        <div class="sponsor-badge" aria-label="Sponsor"></div>
        <div class="sponsor-badge" aria-label="Sponsor"></div>
        <div class="sponsor-badge" aria-label="Sponsor"></div>
      </div>
    </footer>
  </main>
</body>
</html>
```